Safety Consultancy focusing on developing exceptional Safety Leaders

I need a full but simple, modern, catchy website to drive business - my focus is on helping organizations to understand the impact that leaders have on safety performance and how they build the processes to make that happen. I already have great branding (logos) built through ArtisanHive and can provide all narrative to build out the pages

Target Market(s)

Focused internationally. Typical client has a fairly robust and mature safety culture yet lacks the focused effort to develop all levels of leadership in terms of managing safety. Exercising these competencies results in continued development of an organizations safety culture as well as improved safety performance

Industry/Entity Type

all

Coding

Coded - Design and coding required

Number of Pages Required

4 page

Font styles to use
Other font styles liked:
• to match my branding

Colors
0054AA
0677BA
7BADD7
CADEEF
E8F1F8

Requirements
Must have
• Must utilize my current branding, logo, etc. I want to have a page outlining clearly my vision - which I will add to my uploads as we move forward. I need to have a page listing my extensive and unique experience as well as successes
Nice to have
• Want to leave it up to designers - but needs to be simple and easily navigable - hope to have a resource page that I can update myself with safety resource info, reports, etc.

```html
<!DOCTYPE html>
<html lang="en">
<head>
<meta charset="utf-8">
<title>Corvell Ventures International — Safety Leadership</title>
<link href="https://fonts.googleapis.com/css2?family=Lato:wght@300;400;700;900&display=swap" rel="stylesheet">
<style>
:root{
  --navy:#2b3aa0;
  --blue-deep:#0054aa;
  --blue:#0677ba;
  --blue-soft:#7badd7;
  --blue-pale:#cadeef;
  --blue-mist:#e8f1f8;
  --ink:#111;
  --text:#444;
  --white:#fff;
}
*{margin:0;padding:0;box-sizing:border-box}
html,body{width:1200px;height:3514px;overflow:hidden}
body{position:relative;font-family:'Lato',sans-serif;color:var(--ink);background:var(--white)}
.abs{position:absolute}
p{color:var(--text)}
/* brand */
.brand{position:absolute;display:flex;align-items:center;gap:10px;color:var(--navy);font-weight:700}
.brand-mark{width:34px;height:34px;background:var(--navy)}
.brand-name{font-size:30px;line-height:1}
.brand-sub{font-size:13px;display:block;margin-top:3px}
/* header */
.nav a{position:absolute;top:38px;font-size:11.5px;color:var(--ink);text-decoration:none}
.join{position:absolute;left:945px;top:25px;width:105px;height:32px;border-radius:16px;background:var(--navy);color:#fff;font-size:10px;display:flex;align-items:center;justify-content:center}
/* hero */
.hero-bg{left:0;top:0;width:1200px;height:536px;background:linear-gradient(90deg,#ebebeb 0%,#f6f6f6 40%,#d9dbe3 55%,#8d96b8 100%)}
.hero-title{left:149px;top:146px;font-size:50px;font-weight:300;line-height:54px;color:var(--ink)}
.hero-title strong{font-weight:900;color:var(--navy)}
.hero-lead{left:151px;top:346px;width:340px;font-size:11px;font-weight:700;line-height:17px;color:var(--ink)}
.read-more{position:absolute;font-size:14px;color:var(--ink);padding-left:7px;height:38px;display:flex;align-items:center}
.read-more::before{content:"";position:absolute;left:0;top:0;width:12px;height:38px;background:var(--blue)}
.read-more span{position:relative}
.diamond{position:absolute;transform:rotate(45deg)}
/* about */
.about-tab{left:150px;top:640px;width:64px;height:225px;background:var(--blue-soft)}
.about-tab span{position:absolute;left:50%;top:50%;transform:translate(-50%,-50%) rotate(90deg);white-space:nowrap;color:#fff;font-size:25px;font-weight:700}
.about-head{left:258px;top:654px;width:340px;font-size:17.5px;font-weight:700;line-height:20px}
.rule{left:258px;top:747px;width:154px;height:1px;background:#ccc}
.about-text{left:258px;top:778px;width:360px;font-size:11.3px;line-height:20.5px}
/* section 3 */
.office{left:72px;top:964px;width:1054px;height:555px;background:linear-gradient(90deg,#dcd6cd 0%,#ece8e2 45%,#c9d2d6 75%,#6fa7b6 100%)}
.office-lead{left:158px;top:1058px;width:420px;font-size:17.5px;font-weight:700;line-height:23px}
.office-text{left:627px;top:1059px;width:405px;font-size:11px;line-height:20px;color:#222}
.card{position:absolute;background:#fff;box-shadow:0 4px 14px rgba(0,0,0,.12)}
.eyebrow{font-size:23px;font-weight:300;line-height:1;color:var(--ink)}
.card-title{font-size:37px;font-weight:300;line-height:1.1;color:var(--ink)}
.card p{font-size:11px;line-height:21px}
/* experience */
.exp-eyebrow{left:600px;top:1842px;font-size:24px;font-weight:300}
.exp-title{left:600px;top:1872px;font-size:38px;font-weight:300}
.exp-text{left:601px;width:405px;font-size:11px;line-height:21px}
/* verified */
.band{left:80px;top:2320px;width:1037px;height:493px;background:linear-gradient(120deg,#0b2a9a 0%,#0d3fc0 45%,#1857d4 75%,#0a3fb8 100%)}
.band-title{left:153px;top:2410px;font-size:34px;font-weight:300;line-height:42px;color:#fff}
.band-text{left:761px;width:310px;font-size:11px;line-height:20px;color:#fff}
/* contact */
.touch{left:701px;top:2866px;font-size:35px;font-weight:300;line-height:40px}
.field{position:absolute;left:704px;width:346px;border:1px solid #bbb;font-size:10px;color:#888;padding:11px 22px}
.send{left:704px;top:3142px;width:135px;height:42px;background:var(--blue);color:#fff;font-size:15px;font-weight:700;display:flex;align-items:center;justify-content:center}
/* footer */
.foot-line{left:0;top:3257px;width:1200px;height:1px;background:#e2e2e2}
.foot-head{position:absolute;font-size:14px;font-weight:700;color:var(--navy)}
.foot-link{position:absolute;font-size:13px;color:var(--ink)}
.foot-small{position:absolute;font-size:11.5px;line-height:15px;color:var(--ink)}
.copyright{left:0;top:3471px;width:1200px;height:43px;background:var(--navy);color:#fff;font-size:9px;display:flex;align-items:center;justify-content:center}
</style>
</head>
<body>

<!-- HERO -->
<div class="abs hero-bg"></div>
<div class="abs" role="img" aria-label="Photo of a business team walking down an office staircase" style="left:600px;top:0;width:600px;height:536px;background:linear-gradient(160deg,#c8ccd8 0%,#7f89ad 45%,#2c3a8f 80%,#3b4470 100%)"></div>

<div class="brand" style="left:149px;top:24px">
  <span class="brand-mark"></span>
  <span><span class="brand-name">Corvell</span><span class="brand-sub">Ventures International</span></span>
</div>
<nav class="nav">
  <a style="left:470px">Home</a>
  <a style="left:537px">About Us</a>
  <a style="left:622px">Services</a>
  <a style="left:701px">Contact</a>
</nav>
<div class="join">Join Us</div>

<h1 class="abs hero-title">For Your<br><strong>PROTECTION</strong> In<br>The Workplace</h1>
<p class="abs hero-lead">Aliquam erat volutpat. Aliquam vitae tellus feugiat,<br>suscipit ipsum eu, posuere ligula. Praesent nec orci venenatis</p>
<a class="read-more" style="left:149px;top:419px"><span>Read More</span></a>

<div class="diamond" role="img" aria-label="Photo of a security camera on a building" style="left:663px;top:427px;width:224px;height:224px;background:linear-gradient(135deg,#9cc9e6,#3d87b9)"></div>
<div class="diamond" role="img" aria-label="Photo of a security guard with a radio at a monitoring desk" style="left:844px;top:601px;width:222px;height:222px;background:linear-gradient(135deg,#8fa0b0,#2b3545)"></div>

<!-- ABOUT -->
<div class="abs about-tab"><span>01 About</span></div>
<h2 class="abs about-head">Lorem ipsum dolor sit amet, consectetur<br>adipiscing elit. Proin at leo lacus.<br>Aliquam erat volutpat.</h2>
<div class="abs rule"></div>
<p class="abs about-text">Suspendisse ac vehicula lorem. Vestibulum ac porta risus, eu finibus nisl. Vivamus enim turpis, tempus nec rhoncus sagittis, porttitor nec mauris. In et purus eu massa eleifend cursus vel sit amet arcu. Vestibulum hendrerit massa nisi, non venenatis erat elementum</p>

<!-- SERVICES -->
<div class="abs office" role="img" aria-label="Blurred photo of a bright modern office interior"></div>
<h2 class="abs office-lead">Lorem ipsum dolor sit amet, consectetur adipiscing elit. Proin at leo lacus. Aliquam erat volutpat.</h2>
<p class="abs office-text">Suspendisse ac vehicula lorem. Vestibulum ac porta risus, eu finibus nisl. Vivamus enim turpis, tempus nec rhoncus sagittis, porttitor nec mauris. In et purus eu massa eleifend cursus vel sit amet arcu. Vestibulum hendrerit massa nisi, non venenatis erat elementum sit amet. Donec nec sem a diam tempus vulputate. Integer feugiat ultricies urna venenatis imperdiet. Aliquam urna ipsum, hendrerit sit amet rhoncus id, pretium ac diam. Donec id felis tellus.</p>

<div class="card" style="left:150px;top:1250px;width:522px;height:365px">
  <div class="abs" style="left:55px;top:68px">
    <div class="eyebrow">KEEPS YOUR LIVES</div>
    <div class="card-title" style="margin-top:4px">SAFE AND SECURITY</div>
  </div>
  <p class="abs" style="left:55px;top:164px;width:400px">Phasellus congue feugiat pellentesque. Etiam quis quam a ligula placerat gravida. Ut tincidunt massa ut metus lobortis ullamcorper. Ut tempor elit in neque iaculis elementum. Fusce lacinia risus id blandit tempor.</p>
  <a class="read-more" style="left:55px;top:275px"><span>Read More</span></a>
</div>
<div class="abs" style="left:663px;top:1342px;width:15px;height:165px;background:var(--blue)"></div>
<div class="abs" style="left:689px;top:1394px;width:15px;height:86px;background:var(--blue-soft)"></div>

<div class="card" style="left:693px;top:1317px;width:358px;height:374px">
  <div class="abs" style="left:46px;top:56px">
    <div class="eyebrow">WHAT</div>
    <div class="card-title" style="margin-top:4px">WE DO</div>
  </div>
  <p class="abs" style="left:49px;top:151px;width:255px">Phasellus congue feugiat pellentesque. Etiam quis quam a ligula placerat gravida. Ut tincidunt massa ut metus lobortis ullamcorper. Ut tempor elit in neque iaculis elementum. Fusce lacinia risus id blandit tempor.</p>
  <a class="read-more" style="left:49px;top:287px"><span>Read More</span></a>
</div>

<!-- EXPERIENCE -->
<div class="abs" role="img" aria-label="Photo of two business consultants reviewing a tablet" style="left:109px;top:1896px;width:396px;height:424px;background:linear-gradient(160deg,#d9c6b3 0%,#8a6a52 50%,#1f2430 100%)"></div>

<div class="abs exp-eyebrow">WE PROVIDE SERVICE WITH</div>
<h2 class="abs exp-title">20 YEARS EXPERIENCE</h2>
<p class="abs exp-text" style="top:1968px">Nullam gravida leo a aliquet finibus. Nunc quis dolor vehicula, commodo lacus ac, facilisis arcu. Proin libero est, bibendum id gravida quis, porttitor vel est. Nulla convallis vel dui eu rutrum. Curabitur id faucibus erat. Proin malesuada, eros ac feugiat placerat,</p>
<p class="abs exp-text" style="top:2073px">Duis gravida sit amet lacus ut scelerisque. Sed varius lacus ipsum, id facilisis justo maximus non. Suspendisse quis convallis ipsum. In maximus lectus quis quam interdum, sed lobortis eros consequat. Phasellus pulvinar sagittis luctus. Vestibulum et finibus mauris. Curabitur ex tortor, iaculis eget dui eget, posuere bibendum diam.</p>

<!-- VERIFIED -->
<div class="abs band" role="img" aria-label="Blue digital network background"></div>
<h2 class="abs band-title">WE PROVIDE VERIFIED<br>&amp; SECURED SERVICE<br>FOR COMPANY</h2>
<p class="abs band-text" style="top:2521px">Nullam gravida leo a aliquet finibus. Nunc quis dolor vehicula, commodo lacus ac, facilisis arcu. Proin libero est, bibendum id gravida quis, porttitor vel est. Nulla convallis vel dui eu rutrum.</p>
<p class="abs band-text" style="top:2618px">facilisis justo maximus non. Suspendisse quis convallis ipsum. In maximus lectus quis quam interdum, sed lobortis eros consequat. Phasellus pulvinar sagittis luctus. Vestibulum et finibus mauris.</p>

<div class="diamond" role="img" aria-label="Photo of a bodyguard speaking into a radio" style="left:192px;top:2698px;width:222px;height:222px;background:linear-gradient(135deg,#c9ccd0,#3a3d44)"></div>
<div class="diamond" role="img" aria-label="Photo of hands holding a phone with a glowing security shield" style="left:366px;top:2869px;width:222px;height:222px;background:linear-gradient(135deg,#20324a,#3fa6d8 50%,#10151f)"></div>

<!-- CONTACT -->
<h2 class="abs touch">GET<br>IN TOUCH</h2>
<div class="field" style="top:2961px;height:35px">Email</div>
<div class="field" style="top:3005px;height:36px">Phone</div>
<div class="field" style="top:3052px;height:61px">Message</div>
<div class="abs send">SEND</div>

<!-- FOOTER -->
<div class="abs foot-line"></div>
<div class="brand" style="left:149px;top:3307px">
  <span class="brand-mark"></span>
  <span><span class="brand-name">Corvell</span><span class="brand-sub">Ventures International</span></span>
</div>

<div class="foot-head" style="left:432px;top:3287px">QUICK LINKS</div>
<div class="foot-link" style="left:432px;top:3322px">Home</div>
<div class="foot-link" style="left:432px;top:3352px">About Us</div>
<div class="foot-link" style="left:432px;top:3382px">Services</div>
<div class="foot-link" style="left:432px;top:3412px">Contact</div>

<div class="foot-head" style="left:645px;top:3287px">FOLLOW US</div>
<div class="foot-link" style="left:645px;top:3322px">Facebook</div>
<div class="foot-link" style="left:645px;top:3352px">Instagram</div>
<div class="foot-link" style="left:645px;top:3382px">Linkdin</div>

<div class="foot-head" style="left:839px;top:3287px">ADDRESS</div>
<div class="foot-small" style="left:839px;top:3317px">1420 Alder Lane, Harbour Point,<br>British Columbia, Canada V0X 2B7</div>
<div class="foot-head" style="left:839px;top:3357px">PHONE</div>
<div class="foot-small" style="left:839px;top:3376px">1-555-014-2270</div>
<div class="foot-head" style="left:839px;top:3403px">EMAIL</div>
<div class="foot-small" style="left:839px;top:3423px">info@corvell.example</div>

<div class="abs copyright">Copyright © 2024 Corvell Ventures International. All rights reserved.</div>

</body>
</html>
```